Gin Bottle label design

A label for three Gins, 1 Apple flavoured, 1 Bilberry flavoured and one London Dry Gin. All need to incorporate the business logo that i've attached along with the bottle we intend to use. The gin is 40% and will be in a 70cl bottle

```html
<!DOCTYPE html>
<html lang="en">
<head>
<meta charset="utf-8">
<title>London Dry Gin Label</title>
<link href="https://fonts.googleapis.com/css2?family=Oswald:wght@400;500;600&display=swap" rel="stylesheet">
<style>
  :root {
    --canvas: #ffffff;
    --teal: #2fc9c0;
    --teal-deep: #1a9f98;
    --teal-pale: #9fe6df;
    --sage: #b9d6a8;
    --gold: #c99a4a;
    --panel: #ffffff;
    --ink: #2b2b2b;
    --ink-brown: #3a2a1c;
  }
  * { margin: 0; padding: 0; box-sizing: border-box; }
  html, body {
    width: 1200px; height: 1200px; overflow: hidden;
    background: var(--canvas);
  }
  .canvas { position: relative; width: 1200px; height: 1200px; }
  .label {
    position: absolute; left: 175px; top: 105px;
    width: 850px; height: 990px;
  }
  .label-edge { position: absolute; inset: 0; }
  .ornament-frame {
    position: absolute; inset: 14px;
    border-radius: 60px;
    background:
      radial-gradient(ellipse at center, #eef6e6 0%, var(--sage) 60%, var(--teal-pale) 100%);
  }
  .inner-panel {
    position: absolute; left: 126px; top: 115px;
    width: 600px; height: 760px;
    background: linear-gradient(180deg, #ffffff 0%, #f1f3f3 100%);
    border-radius: 40px;
    box-shadow: inset 0 0 0 3px var(--gold);
  }
  .brand {
    position: absolute; left: 0; right: 0; top: 300px;
    display: flex; align-items: center; justify-content: center; gap: 16px;
    font-family: "Oswald", sans-serif; font-weight: 500;
    font-size: 54px; letter-spacing: 3px; color: var(--ink);
  }
  .brand-dot {
    width: 20px; height: 20px; border-radius: 50%;
    background: var(--ink);
  }
  .ribbon { position: absolute; left: 40px; top: 500px; width: 770px; height: 170px; }
  .variety {
    position: absolute; left: 0; right: 0; top: 530px;
    text-align: center;
    font-family: "Oswald", sans-serif; font-weight: 600;
    font-size: 90px; line-height: 1; color: var(--ink);
  }
  .style-name {
    position: absolute; left: 0; right: 0; top: 690px;
    text-align: center;
    font-family: "Oswald", sans-serif; font-weight: 600;
    font-size: 76px; line-height: 1; letter-spacing: 2px; color: var(--ink-brown);
  }
  .spec {
    position: absolute; top: 768px;
    font-family: "Oswald", sans-serif; color: var(--ink);
    text-align: center; line-height: 1;
  }
  .spec-value { display: block; font-size: 36px; font-weight: 400; }
  .spec-unit { display: block; font-size: 14px; margin-top: 4px; letter-spacing: 1px; }
  .spec-abv { left: 230px; }
  .spec-volume { left: 568px; }
</style>
</head>
<body>
<div class="canvas">
  <div class="label">
    <svg class="label-edge" viewBox="0 0 850 990" width="850" height="990" aria-hidden="true">
      <rect x="6" y="6" width="838" height="978" rx="66" fill="none" stroke="var(--teal)" stroke-width="12"/>
      <rect x="16" y="16" width="818" height="958" rx="58" fill="none" stroke="var(--gold)" stroke-width="3"/>
    </svg>
    <div class="ornament-frame" role="img" aria-label="Ornamental border of leafy vines and small flower rosettes in green, teal and gold"></div>
    <div class="inner-panel"></div>

    <div class="brand"><span class="brand-dot"></span>THE OLIVE TABLE</div>

    <svg class="ribbon" viewBox="0 0 770 170" width="770" height="170" aria-hidden="true">
      <polygon points="0,40 90,40 90,130 0,130 30,85" fill="var(--teal-deep)"/>
      <polygon points="770,40 680,40 680,130 770,130 740,85" fill="var(--teal-deep)"/>
      <rect x="60" y="20" width="650" height="120" fill="var(--teal)" stroke="var(--gold)" stroke-width="3"/>
    </svg>
    <div class="variety">LONDON</div>
    <div class="style-name">DRY GIN</div>

    <div class="spec spec-abv"><span class="spec-value">40%</span><span class="spec-unit">ALC VOL</span></div>
    <div class="spec spec-volume"><span class="spec-value">750</span><span class="spec-unit">CL</span></div>
  </div>
</div>
</body>
</html>
```